Redesign of Brochure of company services

We need a redesign a brochure. All of the content on the existing brochure correct, but the design we are not pleased with it. I will provide the previous brochure. Quiet Harbor Fields is Angolan company that provides multiple service ranging providing fruits, vegetables, fisheries, and meat to multiple industries in angola. Quiet Harbor Fields seeks to start delivering or providing their service to home owners looking for fresh products. We want a brochure design that covers all of these aspects.

Target Market(s)

Home owners, middle and upper age mothers, middle and upper class

Industry/Entity Type

Retail

Requirements
Must have
• Logo of the company and the content info
Nice to have
• It's up to you

```html
<!DOCTYPE html>
<html lang="pt">
<head>
<meta charset="utf-8">
<title>Quiet Harbor Fields — Brochura</title>
<link href="https://fonts.googleapis.com/css2?family=Bitter:wght@600;700&family=Lato:wght@400;700&display=swap" rel="stylesheet">
<style>
  :root{
    --orange:#f0582a;
    --orange-deep:#e04a1e;
    --orange-light:#f47a3a;
    --charcoal:#2b2b2b;
    --ink:#333333;
    --paper:#ffffff;
    --paper-grey:#e4e4e4;
    --backdrop:#d9d6d2;
    --fruit-a:#e9a23b;
    --fruit-b:#8db34a;
    --wood:#c89a66;
  }
  *{box-sizing:border-box;margin:0;padding:0}
  html,body{width:1200px;height:875px;overflow:hidden}
  body{background:var(--backdrop);font-family:"Lato",Arial,sans-serif;color:var(--ink);position:relative}

  .trifold{position:absolute;left:47px;top:80px;width:800px;height:570px;background:var(--paper);box-shadow:0 6px 18px rgba(0,0,0,.25);overflow:hidden}
  .trifold-bg{position:absolute;inset:0}
  .abs{position:absolute}

  .tab{position:absolute;top:0;height:38px;border-radius:0 0 10px 10px;color:#fff;font-family:"Bitter",Georgia,serif;font-weight:700;font-size:14px;display:flex;align-items:center;justify-content:center}
  .tab--dark{background:var(--charcoal);left:42px;width:180px}
  .tab--orange{background:var(--orange);left:303px;width:202px}

  .kicker{left:0;width:267px;top:54px;text-align:center;color:var(--orange);font-weight:700;font-size:12px}
  .intro{left:26px;width:225px;top:72px;font-size:10px;line-height:1.25;color:var(--ink)}
  .steps{left:28px;top:119px;list-style:none;font-size:13.5px;line-height:21px}
  .steps span{color:var(--orange);margin-right:3px}

  .photo{position:absolute;border-radius:6px}
  .photo--fruit{left:14px;top:178px;width:246px;height:110px;border-radius:50% 50% 40% 40%;background:radial-gradient(ellipse at 50% 55%,var(--fruit-a),#e2583a 45%,#7fa844 75%,rgba(255,255,255,0) 100%)}
  .photo--crate{left:320px;top:54px;width:180px;height:140px;background:linear-gradient(180deg,#9ac24d 0%,#e0493a 30%,var(--wood) 50%,#b98752 100%)}
  .photo--basket{border-radius:40% 40% 8px 8px;background:radial-gradient(ellipse at 50% 60%,#9fc04a,#e8a13a 40%,#c9473a 65%,rgba(255,255,255,0) 100%)}

  .care{left:28px;top:380px;color:#fff;font-size:15px}
  .care-phone{left:28px;top:404px;color:#fff;font-size:18px}
  .producer{left:28px;top:440px;width:232px;color:#fff;font-family:"Bitter",Georgia,serif;font-weight:700;font-size:12.5px;line-height:1.3;letter-spacing:.3px}
  .discount-title{left:0;width:267px;top:513px;text-align:center;font-weight:700;font-size:12px;color:var(--charcoal)}
  .discount-text{left:28px;width:235px;top:532px;font-size:10.5px;line-height:1.25;color:#fff}

  .values{left:303px;top:364px;font-family:"Bitter",Georgia,serif;font-weight:700;font-size:19px;line-height:24px}
  .values .o{color:var(--orange-light)}
  .values .w{color:#fff}
  .place{left:303px;top:492px;color:#fff;font-weight:700;font-size:15px}
  .contact{left:303px;color:#fff;font-size:12px;display:flex;align-items:center;gap:6px}
  .contact svg{width:10px;height:10px}

  .brand{display:flex;flex-direction:column;align-items:center;gap:6px}
  .brand-mark{width:14px;height:14px;background:var(--orange)}
  .brand-name{font-family:"Lato",Arial,sans-serif;font-weight:400;font-size:17px;color:var(--charcoal);letter-spacing:.2px}
  .brand--inner{left:267px;width:267px;top:218px}

  .cover{position:absolute;top:0;width:266px;height:570px}
  .cover--fold{left:534px}
  .cover--single{left:896px;top:80px;background:var(--paper);box-shadow:0 6px 18px rgba(0,0,0,.25);overflow:hidden}
  .cover-bg{position:absolute;inset:0}
  .cover .brand{position:absolute;left:0;width:100%;top:32px}
  .headline{position:absolute;left:0;width:100%;top:106px;text-align:center;font-family:"Bitter",Georgia,serif;font-weight:700;font-size:25px;line-height:31px}
  .headline .o{color:var(--orange)}
  .headline .d{color:var(--charcoal)}
  .tagline{position:absolute;left:0;width:100%;top:278px;text-align:center;font-size:15px;line-height:20px;color:var(--ink)}
  .cover .photo--basket{left:-10px;top:328px;width:276px;height:196px}
  .cover-email{position:absolute;left:0;width:100%;top:540px;text-align:center;color:var(--orange);font-weight:700;font-size:11px;letter-spacing:1.6px}
</style>
</head>
<body>

<section class="trifold">
  <svg class="trifold-bg" viewBox="0 0 800 570" width="800" height="570" aria-hidden="true">
    <defs>
      <linearGradient id="greyPanel" x1="0" y1="0" x2="1" y2="0">
        <stop offset="0" stop-color="#f6f6f6"/><stop offset="1" stop-color="#dedede"/>
      </linearGradient>
      <linearGradient id="orangeFade" x1="0" y1="0" x2="1" y2="0">
        <stop offset="0" stop-color="#f0582a"/><stop offset="1" stop-color="#f47a3a"/>
      </linearGradient>
      <clipPath id="lowerBand">
        <path d="M0,300 C90,340 250,352 400,332 C440,326 465,318 482,308 C430,380 432,500 505,570 L0,570 Z"/>
      </clipPath>
    </defs>
    <rect x="0" y="0" width="534" height="570" fill="url(#greyPanel)"/>
    <rect x="534" y="0" width="266" height="570" fill="url(#greyPanel)"/>
    <g clip-path="url(#lowerBand)">
      <rect x="0" y="0" width="267" height="570" fill="url(#orangeFade)"/>
      <rect x="267" y="0" width="268" height="570" fill="#2b2b2b"/>
    </g>
    <path d="M0,285 C90,328 250,342 400,322 C440,316 462,308 478,298" fill="none" stroke="#2b2b2b" stroke-width="7"/>
    <path d="M543,570 C462,482 462,312 572,262 C630,236 725,230 800,230 L800,570 Z" fill="#ffffff"/>
    <path d="M523,570 C440,480 440,300 560,245 C620,218 720,212 800,212" fill="none" stroke="#f0582a" stroke-width="7"/>
    <path d="M543,570 C462,482 462,312 572,262 C630,236 725,230 800,230" fill="none" stroke="#2b2b2b" stroke-width="5"/>
  </svg>

  <!-- Panel one -->
  <div class="tab tab--dark">Frescos de Qualidade</div>
  <p class="abs kicker">CONFIE EM QUALIDADE</p>
  <p class="abs intro">A qualidade de todos os frescos distribuídos por nós é verificada para que apenas os produtos aprovados chegem até si.</p>
  <ol class="abs steps">
    <li><span>1.</span>Encomende por telefone</li>
    <li><span>2.</span>Pague no banco</li>
    <li><span>3.</span>Receba os seus frescos</li>
  </ol>
  <div class="photo photo--fruit" role="img" aria-label="Fotografia de frutas variadas: maçãs, laranjas, bananas, uvas e frutos vermelhos"></div>
  <p class="abs care">Manuseamos com cuidado</p>
  <p class="abs care-phone">+244 923 410 582</p>
  <p class="abs producer">Se for produtor e deseja comercializar os seus produtos de forma segura, contacte-nos hoje!</p>
  <p class="abs discount-title">FAZEMOS DESCONTOS</p>
  <p class="abs discount-text">Fazemos descontos a clientes com contratos de fornecimento contínuo.</p>

  <!-- Panel two -->
  <div class="tab tab--orange">Entregamos à sua porta</div>
  <div class="photo photo--crate" role="img" aria-label="Fotografia de caixa de madeira com legumes frescos"></div>
  <div class="abs brand brand--inner">
    <span class="brand-mark"></span>
    <span class="brand-name">Quiet Harbor Fields</span>
  </div>
  <p class="abs values"><span class="o">Qualidade.</span><br><span class="w">Rapidez.</span><br><span class="o">Satisfação</span></p>
  <p class="abs place">Maianga, Luanda</p>
  <p class="abs contact" style="top:516px">
    <svg viewBox="0 0 10 10" aria-hidden="true"><path d="M2,0.5 L3.6,2.6 L2.8,3.6 C3.4,5 4.9,6.5 6.4,7.2 L7.4,6.4 L9.5,8 L8.4,9.5 C4.5,9.2 0.8,5.5 0.5,1.6 Z" fill="#f0582a"/></svg>
    +244 923 410 582
  </p>
  <p class="abs contact" style="top:536px">
    <svg viewBox="0 0 10 10" aria-hidden="true"><rect x="0.5" y="2" width="9" height="6.5" fill="#f0582a"/><path d="M0.5,2 L5,5.6 L9.5,2" fill="none" stroke="#2b2b2b" stroke-width="0.8"/></svg>
    contacto@quietharbor.ao
  </p>

  <!-- Cover panel -->
  <div class="cover cover--fold">
    <div class="brand">
      <span class="brand-mark"></span>
      <span class="brand-name">Quiet Harbor Fields</span>
    </div>
    <h1 class="headline"><span class="o">Hortaliças</span><br><span class="d">Frutas Carnes</span><br><span class="o">Peixes Mariscos</span></h1>
    <p class="tagline">Levamos produtos frescos<br>Nacionais à sua porta.</p>
    <div class="photo photo--basket" role="img" aria-label="Fotografia de cesto com frutas: ananás, maçãs, uvas, melão, bananas e laranjas"></div>
    <p class="cover-email">contacto@quietharbor.ao</p>
  </div>
</section>

<section class="cover cover--single">
  <svg class="cover-bg" viewBox="0 0 266 570" width="266" height="570" aria-hidden="true">
    <defs>
      <linearGradient id="greyCover" x1="0" y1="0" x2="1" y2="0">
        <stop offset="0" stop-color="#f6f6f6"/><stop offset="1" stop-color="#dedede"/>
      </linearGradient>
    </defs>
    <rect width="266" height="570" fill="url(#greyCover)"/>
    <path d="M0,282 C60,236 200,228 266,262 L266,570 L0,570 Z" fill="#ffffff"/>
    <path d="M0,266 C60,218 200,210 266,244" fill="none" stroke="#f0582a" stroke-width="7"/>
    <path d="M0,282 C60,236 200,228 266,262" fill="none" stroke="#2b2b2b" stroke-width="5"/>
  </svg>
  <div class="brand">
    <span class="brand-mark"></span>
    <span class="brand-name">Quiet Harbor Fields</span>
  </div>
  <h1 class="headline"><span class="o">Hortaliças</span><br><span class="d">Frutas Carnes</span><br><span class="o">Peixes Mariscos</span></h1>
  <p class="tagline">Levamos produtos frescos<br>Nacionais à sua porta.</p>
  <div class="photo photo--basket" role="img" aria-label="Fotografia de cesto com frutas: ananás, maçãs, uvas, melão, bananas e laranjas"></div>
  <p class="cover-email">contacto@quietharbor.ao</p>
</section>

</body>
</html>
```